Startup online payment business - Sporting / Golf, Swift Tee payment

Background:
Our business name is "Swift Tee" we provide online payments for golfing services via our website. We currently have a logo used on our website. No other design style has been developed. Our aim is to remove cash payments for service at golf clubs.

Our Key Values:
Quick and easy
Formal and polite
Fun with professional boundary
Mate-ship relationships
100% online digital

What we want from you:
Marketing design to be used on posters and stickers in a retail setting to direct customers to our online payment Chanel.
Design must incorporate attached logo, URL swifttee.com.au and our key values can act as a guide the type of design. We have used color Hex#007672 for logo background. We are open to use other colors.

Target Market(s)

Golf clubs and golf players

Industry/Entity Type

Golf Course

Font styles to use
Sans Serif

Requirements
Must have
• Directions to online payment via URL: swifttee.com.au
Nice to have
• We like the idea of the slogan: No Cash - No worries. Have attached home screen that will be available from URL link. Consideration if using mobile phone in image. Push the online payment and steps 1. Visit swifttee.com 2. Select club 3. Confirm payment
Should not have
• Cartoons

```html
<!DOCTYPE html>
<html lang="en">
<head>
<meta charset="utf-8">
<title>Swift Tee – No Cash No Worries</title>
<link href="https://fonts.googleapis.com/css2?family=Barlow+Condensed:wght@500;600;800&display=swap" rel="stylesheet">
<style>
  :root {
    --page: #e9ecea;
    --teal: #127a72;
    --teal-deep: #0c5f58;
    --teal-dark: #074741;
    --teal-light: #2a8f84;
    --grass: #0f5a33;
    --white: #ffffff;
  }
  * { margin: 0; padding: 0; box-sizing: border-box; }
  html, body {
    width: 1200px; height: 878px; overflow: hidden;
    background: var(--page);
  }
  .poster {
    position: absolute; left: 342px; top: 19px;
    width: 516px; height: 840px;
    background: var(--teal);
    overflow: hidden;
    font-family: "Barlow Condensed", sans-serif;
    color: var(--white);
  }
  .money-backdrop {
    position: absolute; left: 0; top: 0; width: 100%; height: 418px;
    background: linear-gradient(180deg, #1b847b 0%, #157d75 60%, var(--teal) 100%);
  }
  .brand-tab {
    position: absolute; left: 164px; top: -3px; width: 205px; height: 196px;
    background: var(--teal);
    border: 3px solid var(--white); border-top: none;
    display: flex; flex-direction: column; align-items: center; justify-content: center;
    font-weight: 500; color: var(--white);
  }
  .brand-name { font-size: 60px; letter-spacing: 3px; line-height: 1; }
  .brand-sub { font-size: 20px; letter-spacing: 8px; margin-top: 14px; line-height: 1; }
  .headline {
    position: absolute; left: 0; top: 196px; width: 100%;
    text-align: center; font-weight: 800; text-transform: uppercase;
    font-size: 104px; line-height: 100px; letter-spacing: -1px;
    text-shadow: 2px 3px 4px rgba(0,0,0,0.35);
  }
  .headline-rule { position: absolute; left: 39px; top: 410px; }
  .golf-scene {
    position: absolute; left: 10px; top: 440px; width: 250px; height: 320px;
    border-radius: 40px;
    background:
      radial-gradient(circle at 38% 74%, #3a9a8d 0%, #2a8b80 16%, rgba(42,139,128,0) 30%),
      linear-gradient(160deg, rgba(12,95,88,0) 0%, var(--teal-deep) 55%, #0b5550 100%);
  }
  .grass-strip {
    position: absolute; left: 0; top: 738px; width: 100%; height: 102px;
    background: linear-gradient(180deg, #2f7d4e 0%, var(--grass) 55%, #0a4326 100%);
  }
  .site-url {
    position: absolute; left: 0; top: 790px; width: 100%;
    text-align: center; font-weight: 600; font-size: 30px; line-height: 36px;
    letter-spacing: 1px;
  }
  .values {
    position: absolute; left: 251px; top: 518px; list-style: none;
    font-weight: 600; font-size: 26px; line-height: 34px;
  }
  .values li { position: relative; padding-left: 40px; }
  .values li svg { position: absolute; left: 0; top: 10px; }
</style>
</head>
<body>
  <main class="poster">
    <div class="money-backdrop" role="img" aria-label="Teal-toned photo of scattered banknotes"></div>

    <div class="brand-tab">
      <span class="brand-name">SWIFT</span>
      <span class="brand-sub">TEE</span>
    </div>

    <h1 class="headline">No Cash<br>No Worries</h1>

    <svg class="headline-rule" width="444" height="22" viewBox="0 0 444 22" aria-hidden="true">
      <path d="M2 19 Q222 -6 442 15" fill="none" stroke="#fff" stroke-width="5" stroke-linecap="round"/>
    </svg>

    <div class="golf-scene" role="img" aria-label="Photo of a golf iron about to strike a ball on a tee"></div>
    <div class="grass-strip" role="img" aria-label="Photo of green grass along the bottom"></div>

    <ul class="values">
      <li><svg width="32" height="18" viewBox="0 0 32 18"><path d="M0 2 L32 0 L12 18 Z" fill="#fff"/></svg>Quick and easy</li>
      <li><svg width="32" height="18" viewBox="0 0 32 18"><path d="M0 2 L32 0 L12 18 Z" fill="#fff"/></svg>Formal and polite</li>
      <li><svg width="32" height="18" viewBox="0 0 32 18"><path d="M0 2 L32 0 L12 18 Z" fill="#fff"/></svg>Fun with professional<br>boundary</li>
      <li><svg width="32" height="18" viewBox="0 0 32 18"><path d="M0 2 L32 0 L12 18 Z" fill="#fff"/></svg>Mate-ship relationships</li>
      <li><svg width="32" height="18" viewBox="0 0 32 18"><path d="M0 2 L32 0 L12 18 Z" fill="#fff"/></svg>100% online digital</li>
    </ul>

    <p class="site-url">swifttee.com.au</p>
  </main>
</body>
</html>
```